Thank You For Shopping / Hair Care Tips

I need “Thank You For Shopping”
Post cards made for my hair business !
I added pictures of post cards that I really like . I also added my LuzeKora Wigs logo for you guys to use

I want the backside of the flyer to have hair care tips !
I want people to have full directions on how to care for their wigs

Target Market(s)

Im marking to young woman to older middle aged woman
Ages 23-66 . I want my flyer to look mature And classy

Industry/Entity Type

Hair And Beauty

Font styles to use
Serif
Script

Colors
e34699
e34298
e34398

Requirements
Must have
• The flyer must have the Instagram logo with my Instagram name next to it @luze.kora.wigs__
• Also it must have my “Luze Kora Wigs” logo that I’ve uploaded in the pictures section .
• Flyer had to be two sides . One side “ thank you for shopping “ side two “hair care tips”
• My website must be on the flyer - www.luzekorawigs.example
• The flyer must match the colors of my logo
• All white . With the pink and glitter sliver you see on my logo
Nice to have
• Nice to have a glitter border
Should not have
• The flyer should not have different colors that don’t match my logo
• It shouldn’t be made without having my Instagram or website on the flyer

```html
<!DOCTYPE html>
<html lang="en">
<head>
<meta charset="utf-8">
<title>LuzeKora Wigs – Thank You Postcard</title>
<link rel="stylesheet" href="https://fonts.googleapis.com/css2?family=Great+Vibes&family=Montserrat:wght@500;700;800&display=swap">
<style>
  :root {
    --bg: #f1f1f0;
    --glitter-light: #f27ab8;
    --glitter-mid: #e34699;
    --glitter-deep: #c2257a;
    --panel-light: #fde6f1;
    --panel-mid: #f8c6de;
    --panel-edge: #e34298;
    --band-deep: #a8125f;
    --band-mid: #d22f87;
    --ink-pink: #e34398;
    --ink-dark: #4a4a4a;
    --white: #ffffff;
  }
  * { box-sizing: border-box; margin: 0; padding: 0; }
  html, body { width: 1200px; height: 900px; overflow: hidden; }
  body {
    background: var(--bg);
    font-family: "Montserrat", Arial, sans-serif;
    display: flex;
    align-items: center;
    justify-content: center;
    gap: 40px;
  }
  .postcard {
    position: relative;
    width: 560px;
    height: 400px;
    padding: 28px;
    border-radius: 6px;
    background: radial-gradient(circle at 30% 30%, var(--glitter-light), var(--glitter-mid) 55%, var(--glitter-deep));
    box-shadow: 0 6px 18px rgba(0,0,0,0.15);
  }
  .postcard__panel {
    position: relative;
    width: 100%;
    height: 100%;
    border-radius: 16px;
    border: 3px solid var(--panel-edge);
    background: linear-gradient(160deg, var(--panel-light), var(--panel-mid));
    overflow: hidden;
  }
  .brand-mark {
    position: absolute;
    color: var(--ink-dark);
    font-weight: 800;
    font-size: 15px;
    letter-spacing: 0.3px;
    display: flex;
    align-items: center;
    gap: 6px;
    white-space: nowrap;
  }
  .brand-mark__dot {
    width: 9px; height: 9px; border-radius: 50%;
    background: var(--ink-pink);
  }

  /* front */
  .front__headline {
    position: absolute;
    left: 50px; top: 34px;
    width: 300px;
    font-family: "Great Vibes", cursive;
    font-weight: 400;
    font-size: 62px;
    line-height: 0.92;
    color: var(--ink-pink);
    text-align: center;
  }
  .front__headline span { display: block; }
  .front .brand-mark { right: 22px; bottom: 58px; }
  .front__contacts {
    position: absolute;
    left: 14px; right: 14px; bottom: 12px;
    display: flex;
    gap: 22px;
    font-size: 11px;
    font-weight: 500;
    color: var(--ink-dark);
  }
  .contact { display: flex; align-items: center; gap: 5px; }
  .contact__square {
    width: 11px; height: 11px; border-radius: 2px; background: var(--ink-dark);
  }

  /* back */
  .back__band {
    margin-top: 14px;
    height: 36px;
    background: linear-gradient(90deg, var(--band-deep), var(--band-mid));
    color: var(--white);
    font-weight: 800;
    font-size: 17px;
    display: flex;
    align-items: center;
    justify-content: center;
  }
  .tips {
    list-style: none;
    margin: 16px 0 0 8px;
    width: 360px;
    text-align: center;
    color: var(--ink-pink);
    font-weight: 700;
    font-size: 12px;
    line-height: 21px;
  }
  .back .brand-mark { right: 12px; top: 170px; font-size: 13px; }
</style>
</head>
<body>

  <section class="postcard front" aria-label="Postcard front">
    <div class="postcard__panel">
      <h1 class="front__headline"><span>thank you</span><span>for</span><span>shopping</span></h1>
      <div class="brand-mark"><span class="brand-mark__dot"></span>LuzeKora Wigs</div>
      <div class="front__contacts">
        <span class="contact"><span class="contact__square"></span>@luze.kora.wigs__</span>
        <span class="contact">
          <svg width="11" height="11" viewBox="0 0 12 12" aria-hidden="true">
            <circle cx="6" cy="6" r="5" fill="none" stroke="#4a4a4a" stroke-width="1.2"/>
            <ellipse cx="6" cy="6" rx="2.2" ry="5" fill="none" stroke="#4a4a4a" stroke-width="1"/>
            <line x1="1" y1="6" x2="11" y2="6" stroke="#4a4a4a" stroke-width="1"/>
          </svg>
          www.luzekorawigs.example
        </span>
      </div>
    </div>
  </section>

  <section class="postcard back" aria-label="Postcard back">
    <div class="postcard__panel">
      <h2 class="back__band">10 Tips to Longer Stronger Hair</h2>
      <ol class="tips">
        <li>1. Deep Condition your hair</li>
        <li>2. Deep Condition with heat</li>
        <li>3. Deep Condition with a moisturizing conditioner</li>
        <li>4. Deep Condition with a protein conditioner</li>
        <li>5. Deep Condition when you are not in the mood</li>
        <li>6. Deep Condition when your hair feels dry</li>
        <li>7. Deep Condition when your hair feels great</li>
        <li>8. Deep Condition a little bit more</li>
        <li>9. Deep Condition even more</li>
        <li>10. Just Deep Condition !</li>
      </ol>
      <div class="brand-mark"><span class="brand-mark__dot"></span>LuzeKora Wigs</div>
    </div>
  </section>

</body>
</html>
```